Postcard, Gift Card/Envelope
Looking for Trendy and Sexy material to represent a High End Salon and Spa.
I'd like to wrap up this project before the expiration ... please put forth your best efforts sooner rather than later.
RT3192 - I love your use of the salon pics on the back!! The front: the main message "We Have Moved!" doesn't jump out to the reader.
Thanks, Few things. Postcard: I like the impact of the new "we have moved", but types style might clash a bit? Envelope: Add the hawthorne location and phone numbers on olutside, but you can make them smaller ... and Make "look and feel your best" in italics. Giftcard: must have two phone numbers underneath the addresses (they are two separate locations). Last, we recently rebranded ... so add "formerly Marisol Glow Studio" in italics below the main logo of the postcard.
Thanks for the fine efforts. For the back of postcard, I like draft #1 with the offer featured on top. I was thinking that the front could have a smaller element "TAN FREE (see offer on back") that doesn’t take away from the clean look of the front. I’d also like to promote and in store promotional, FREE LEG TAN THURDSAY (every Thursday till March 15). I added a pic of the leg tanner to include if you think it won’t be too busy. I also added another pic of the tanning booths that might be used (only at your discretion)
The Gift card should be one sided, needs to include address/phones of both salons and add a line for Date. Try using a more luxurious font to represent the quality of the business. The envelope is not for mailing, simply for presentation … so perhaps use the graphics that you used for the “other side” of the gift card with the tag line “Look and Feel Your Best”.
Thanks! When you get a chance can you check your messages in the top right-hand corner of the page
Thanks for your submission. I like it. I'd like to reference to the Free week offer somewhere on the front. Also, see if there is a way to make the "We Have Moved" even more prominent. I think it's fairly prominent in your first draft, but want to see a few different levels of POP.

```html
<!DOCTYPE html>
<html lang="en">
<head>
<meta charset="utf-8">
<title>Solara Tan &amp; Spa — Stationery Set</title>
<link href="https://fonts.googleapis.com/css2?family=Cinzel:wght@400;600&family=Anton&family=Playfair+Display:ital,wght@0,400;1,400&family=Open+Sans:ital,wght@0,400;0,700;1,400&display=swap" rel="stylesheet">
<style>
:root{
  --board:#1c1c1e;
  --sky-top:#7fb6e3;
  --sky-light:#d9ecf9;
  --orange:#f08a1c;
  --red-orange:#e0541b;
  --green:#4aa62c;
  --green-dark:#2f7d1d;
  --white:#ffffff;
  --ink:#3b3b3b;
  --brand:#7a8a2a;
  --muted:#8d8d8d;
  --photo-skin:#c98f6c;
  --photo-sand:#e4c9a4;
}
*{box-sizing:border-box;margin:0;padding:0}
html,body{width:1200px;height:862px;overflow:hidden;background:var(--board)}
body{position:relative;font-family:"Open Sans",sans-serif;color:var(--ink)}
.piece{position:absolute;overflow:hidden;background:var(--white);box-shadow:0 4px 14px rgba(0,0,0,.55)}
.abs{position:absolute}
.swoosh{position:absolute;left:0;width:100%}
.brand{font-family:"Cinzel",serif;font-weight:600;color:var(--brand);letter-spacing:1px;white-space:nowrap;display:flex;align-items:center;gap:8px}
.brand .dot{width:11px;height:11px;border-radius:50%;background:var(--orange);display:inline-block}
.photo{position:absolute}

/* Postcard front */
.postcard-front{left:48px;top:24px;width:518px;height:408px;background:linear-gradient(180deg,var(--sky-top) 0%,var(--sky-light) 50%,var(--white) 75%)}
.postcard-front .tag{right:0;top:10px;background:var(--orange);color:var(--white);font-family:"Anton",sans-serif;font-size:18px;letter-spacing:1px;padding:4px 14px}
.postcard-front .brand{left:46px;top:40px;font-size:28px}
.postcard-front .headline{left:18px;top:118px;font-family:"Anton",sans-serif;font-style:italic;font-size:42px;color:var(--red-orange);letter-spacing:1px;text-shadow:1px 2px 0 rgba(120,40,0,.35);transform:skewX(-6deg);white-space:nowrap}
.postcard-front .distance{left:22px;top:180px;font-family:"Playfair Display",serif;font-size:17px;color:var(--orange);white-space:nowrap}
.postcard-front .map{left:356px;top:112px;width:148px;height:140px;background:linear-gradient(135deg,#e7e9e4,#cfd6cf);border:3px solid var(--white);border-radius:6px}
.postcard-front .map-keys{left:346px;top:92px;font-size:9px;color:var(--ink);display:flex;gap:14px}
.map-keys span::before{content:"";display:inline-block;width:8px;height:8px;border-radius:50%;margin-right:4px;vertical-align:-1px;background:var(--green)}
.map-keys span.old::before{background:var(--red-orange)}
.postcard-front .model{left:0;top:250px;width:215px;height:158px;background:linear-gradient(180deg,var(--photo-sand),var(--photo-skin))}
.postcard-front .tan-free{left:330px;top:340px;width:150px;text-align:center;color:var(--ink);font-family:"Anton",sans-serif;font-size:20px;letter-spacing:1px;line-height:1}
.tan-free small{display:block;font-family:"Open Sans",sans-serif;font-size:11px;letter-spacing:0;margin-top:4px}

/* Gift certificate */
.gift{left:588px;top:29px;width:564px;height:240px;background:linear-gradient(160deg,var(--sky-light) 0%,var(--white) 45%)}
.gift .brand{left:32px;top:24px;font-size:19px}
.gift .tagline{left:32px;top:54px;font-family:"Playfair Display",serif;font-style:italic;font-size:15px;color:var(--ink)}
.gift .locations{left:32px;top:100px;display:flex;gap:26px;font-size:8.5px;line-height:1.35;color:var(--ink)}
.gift .title{left:300px;top:20px;font-family:"Cinzel",serif;font-size:23px;color:var(--ink);letter-spacing:1.5px}
.gift .fields{left:300px;top:58px;width:230px}
.gift .field{display:flex;align-items:flex-end;height:18px;font-family:"Playfair Display",serif;font-style:italic;font-size:12px;color:var(--ink)}
.gift .field span{width:64px}
.gift .field i{flex:1;border-bottom:1px solid var(--muted);height:12px}
.gift .contact{left:0;width:100%;top:204px;text-align:center;color:var(--white);font-size:11px;line-height:1.35;z-index:2}

/* Envelope front */
.env-front{left:588px;top:365px;width:533px;height:211px}
.env-front .brand{left:24px;top:26px;font-size:17px}
.env-front .address{left:24px;top:54px;font-size:8px;line-height:1.4;color:var(--ink)}

/* Envelope back */
.env-back{left:588px;top:588px;width:533px;height:204px;background:#f7f7f7}
.env-back .brand{left:0;width:100%;justify-content:center;top:80px;font-size:14px}

/* Postcard back */
.postcard-back{left:48px;top:451px;width:518px;height:401px}
.postcard-back .brand{left:24px;top:20px;font-size:18px}
.postcard-back .offer{left:20px;top:56px;width:210px;text-align:center}
.offer .big{font-family:"Anton",sans-serif;font-style:italic;font-size:30px;color:var(--red-orange);transform:skewX(-6deg);display:block;line-height:1.05}
.offer .sub{font-family:"Playfair Display",serif;font-size:16px;color:var(--orange)}
.offer p{font-size:7.5px;color:var(--ink);margin-top:6px;line-height:1.35}
.postcard-back .model{left:0;top:150px;width:110px;height:192px;background:linear-gradient(180deg,var(--photo-sand),var(--photo-skin))}
.postcard-back .services{left:118px;top:155px;width:125px;font-size:9px;line-height:1.5;color:var(--ink)}
.services h3{font-size:11px;font-weight:700;color:var(--green-dark)}
.services li{list-style:none;padding-left:10px;position:relative}
.services li::before{content:"";position:absolute;left:0;top:6px;width:5px;height:5px;border-radius:50%;background:var(--orange)}
.postcard-back .booth{left:114px;top:245px;width:118px;height:92px;background:linear-gradient(135deg,#dfe4ea,#9fb0c2);border:2px solid var(--white)}
.postcard-back .leg-band{left:0;top:362px;width:245px;height:39px;background:var(--green);color:var(--white);text-align:center;font-family:"Anton",sans-serif;font-size:15px;letter-spacing:.5px;line-height:1.1;padding-top:4px}
.leg-band small{display:block;font-family:"Open Sans",sans-serif;font-size:8px;letter-spacing:0}
.postcard-back .web{left:6px;top:348px;font-size:7px;color:var(--ink)}
.postcard-back .return{left:272px;top:24px;font-size:8.5px;line-height:1.4;color:var(--ink)}
.postcard-back .stamp{right:20px;top:16px;width:60px;height:66px;background:#d6d6d6}
</style>
</head>
<body>

<!-- Postcard front -->
<section class="piece postcard-front" aria-label="Postcard front">
  <div class="abs tag">NEW SALON</div>
  <div class="abs brand"><span class="dot"></span>SOLARA TAN &amp; SPA</div>
  <div class="abs map-keys"><span>New Location</span><span class="old">Old Location</span></div>
  <div class="abs map" role="img" aria-label="Street map showing the old and new salon locations"></div>
  <h1 class="abs headline">WE HAVE MOVED!</h1>
  <p class="abs distance">Exactly 1.2 miles west on Route 12</p>
  <svg class="swoosh" style="top:230px;height:110px" viewBox="0 0 100 30" preserveAspectRatio="none" aria-hidden="true">
    <path d="M0 14 C30 4 60 22 100 4 L100 9 C60 27 30 9 0 19Z" fill="var(--orange)"/>
    <path d="M0 21 C30 11 60 29 100 11 L100 22 C60 34 30 20 0 30Z" fill="var(--green)"/>
  </svg>
  <div class="photo model" role="img" aria-label="Photo of a tanned woman in a bikini lying on her front"></div>
  <div class="abs tan-free">TAN FREE<small>(see offer on back)</small></div>
</section>

<!-- Gift certificate -->
<section class="piece gift" aria-label="Gift certificate">
  <div class="abs brand"><span class="dot"></span>SOLARA TAN &amp; SPA</div>
  <p class="abs tagline">Look and Feel Your Best</p>
  <div class="abs locations">
    <p>220 Harbor Road West<br>Lindale, NJ 07100</p>
    <p>48 Maple Avenue<br>Fairbrook, NJ 07200</p>
  </div>
  <h2 class="abs title">GIFT CERTIFICATE</h2>
  <div class="abs fields">
    <div class="field"><span>To</span><i></i></div>
    <div class="field"><span>From</span><i></i></div>
    <div class="field"><span>Date</span><i></i></div>
    <div class="field"><span>Amount</span><i></i></div>
    <div class="field"><span>Signature</span><i></i></div>
  </div>
  <svg class="swoosh" style="top:140px;height:100px" viewBox="0 0 100 40" preserveAspectRatio="none" aria-hidden="true">
    <path d="M0 10 C35 28 65 0 100 12 L100 40 L0 40Z" fill="var(--orange)"/>
    <path d="M0 13 C35 31 65 3 100 15 L100 40 L0 40Z" fill="var(--white)"/>
    <path d="M0 16 C35 34 65 6 100 18 L100 40 L0 40Z" fill="var(--green)"/>
  </svg>
  <p class="abs contact">Phone 555.014.2260<br>www.solaratanspa.com</p>
</section>

<!-- Envelope front -->
<section class="piece env-front" aria-label="Envelope front">
  <div class="abs brand"><span class="dot"></span>SOLARA TAN &amp; SPA</div>
  <p class="abs address">220 Harbor Road West<br>Lindale, NJ 07100</p>
  <svg class="swoosh" style="top:120px;height:91px" viewBox="0 0 100 40" preserveAspectRatio="none" aria-hidden="true">
    <path d="M0 30 C40 40 70 4 100 6 L100 40 L0 40Z" fill="var(--orange)"/>
    <path d="M0 33 C40 42 70 9 100 11 L100 40 L0 40Z" fill="var(--white)"/>
    <path d="M0 36 C40 44 70 14 100 16 L100 40 L0 40Z" fill="var(--green)"/>
  </svg>
</section>

<!-- Envelope back -->
<section class="piece env-back" aria-label="Envelope back">
  <svg class="swoosh" style="top:0;height:60px" viewBox="0 0 100 20" preserveAspectRatio="none" aria-hidden="true">
    <path d="M0 0 L100 0 L100 8 C70 18 30 2 0 12Z" fill="var(--green)"/>
    <path d="M0 12 C30 2 70 18 100 8 L100 10 C70 20 30 4 0 14Z" fill="var(--orange)"/>
  </svg>
  <svg class="abs" style="left:0;top:0" width="533" height="204" viewBox="0 0 533 204" aria-hidden="true">
    <path d="M0 10 L266 120 L533 10" fill="none" stroke="#d4d4d4" stroke-width="1.5"/>
    <path d="M0 204 L200 95 M533 204 L333 95" fill="none" stroke="#e3e3e3" stroke-width="1"/>
  </svg>
  <div class="abs brand"><span class="dot"></span>SOLARA</div>
</section>

<!-- Postcard back -->
<section class="piece postcard-back" aria-label="Postcard back">
  <div class="abs brand"><span class="dot"></span>SOLARA TAN &amp; SPA</div>
  <div class="abs offer">
    <span class="big">ONE FREE WEEK</span>
    <span class="sub">of tanning</span>
    <p>New clients only. Bring this card to either salon to redeem your free week.</p>
  </div>
  <div class="photo model" role="img" aria-label="Photo of a smiling woman with a tan"></div>
  <div class="abs services">
    <h3>Services:</h3>
    <ul>
      <li>Adding Custom Airbrush</li>
      <li>Waxing and Teeth Whitening!</li>
      <li>(April of 2012)</li>
    </ul>
  </div>
  <div class="photo booth" role="img" aria-label="Photo of the salon's tanning booths"></div>
  <p class="abs web">www.solaratanspa.com</p>
  <div class="abs leg-band">FREE LEG TAN THURSDAY<small>every Thursday till March 15</small></div>
  <p class="abs return">220 Harbor Road West<br>Lindale, NJ 07100</p>
  <div class="abs stamp" aria-label="Stamp area"></div>
</section>

</body>
</html>
```